First Breath Diving Kelp Dive Bonaire

Kelp Dive is looking for a great flyer to promote our First Breath Diving around Bonaire, the Caribbean.

Bonaire is shore dive capital of the world.
Our guests rent a pick-up truck. we would like to inform them about the possibilities of the First Breath Dive.

We have the logo, images and text available. Its the catchy and mind blowing design we are looking for to create an eye-catch flyer.
One side will be in English, the other side will be in Dutch.

Target Market(s)

Visitors (non divers) of the island Bonaire

Industry/Entity Type

Diving industry

Font styles to use
Sans Serif

Colors
0094D4
00A9DD
6FCCEA
C7EBF8
E9F6FB
F0912C
F2A743
F7CA91
FBE8D2
FDF5EE

Requirements
Must have
• The picture with the car and divers next to it is mandatory. Inspire to go for a first breath dive, show the beauty under water, easy to come dive with us, just takes half a day
Should not have
• Should not have pictures taken not around Bonaire.

```html
<!DOCTYPE html>
<html lang="en">
<head>
<meta charset="utf-8">
<title>First Breath Diving – Kelp Dive Bonaire flyer</title>
<link href="https://fonts.googleapis.com/css2?family=Montserrat:wght@300;400;500;600&display=swap" rel="stylesheet">
<style>
  :root{
    --backdrop:#808080;
    --paper:#ffffff;
    --sky:#00A9DD;
    --ocean:#0094D4;
    --deep:#1a6fc4;
    --navy:#0d2c57;
    --ink:#1d1d1d;
    --muted-blue:#27a7dd;
    --reef-top:#3f78c0;
    --reef-mid:#6d8fb8;
    --reef-sand:#b7b4ad;
  }
  *{box-sizing:border-box;margin:0;padding:0}
  html,body{width:1200px;height:863px;overflow:hidden;background:var(--backdrop)}
  body{position:relative;font-family:"Montserrat",sans-serif;color:var(--ink)}

  .flyer{position:absolute;top:85px;width:480px;height:678px;background:var(--paper);overflow:hidden}
  .flyer--en{left:81px}
  .flyer--nl{left:640px}

  .hero{position:absolute;left:0;top:0;width:480px;height:340px}
  .hero svg{position:absolute;inset:0}

  .brand{position:absolute;right:22px;top:14px;width:60px;text-align:center}
  .brand__dot{display:block;width:38px;height:38px;margin:0 auto 4px;border-radius:50%;background:var(--deep)}
  .brand__name{font-weight:600;font-size:9px;color:var(--navy);white-space:nowrap}

  .title{position:absolute;left:38px;top:112px;color:#fff;font-weight:300;line-height:1}
  .title__small{display:block;font-size:27px;letter-spacing:1px}
  .title__big{display:block;font-size:50px;letter-spacing:0.5px;margin-top:5px}
  .tagline{position:absolute;left:39px;top:200px;color:#fff;font-weight:600;font-size:10.5px;white-space:nowrap;text-shadow:0 1px 2px rgba(0,0,0,.35)}

  .callout{position:absolute;right:22px;color:#fff;font-weight:600;text-align:right}
  .flyer--en .callout{top:159px;font-size:10.6px;line-height:16.9px}
  .flyer--nl .callout{top:161px;font-size:10.6px;line-height:14.5px}

  .social{position:absolute;left:28px;top:292px}
  .social__dot{position:absolute;width:17px;height:17px;border-radius:50%;background:#fff}
  .social__dot:nth-child(1){left:0;top:0}
  .social__dot:nth-child(2){left:36px;top:12px}
  .social__dot:nth-child(3){left:66px;top:22px}

  .photo{position:absolute;display:block}
  .photo--gear{left:281px;top:337px;width:168px;height:86px;background:linear-gradient(180deg,#a9d2dc 0%,#dfeff0 45%,#4b4a48 70%,#d6d1c6 100%)}
  .photo--truck{left:29px;top:406px;width:221px;height:120px;background:linear-gradient(180deg,#7fb6e0 0%,#3da3c8 35%,#9fd2d6 50%,#e5e3dc 70%,#d9d5cc 100%)}
  .flyer--nl .photo--truck{left:28px;top:423px;width:225px;height:103px}
  .photo--turtle{left:281px;top:526px;width:168px;height:95px;background:linear-gradient(180deg,#4d8ed6 0%,#6fa8d8 35%,#8c8ba6 65%,#b8a27a 100%)}

  .section{position:absolute}
  .section__head{font-weight:500;font-size:11.6px;color:var(--muted-blue);text-transform:uppercase;line-height:1;white-space:nowrap}
  .section__body{font-size:7.4px;line-height:9.6px;margin-top:2px}
  .section__list{list-style:none;font-size:6.8px;line-height:9.6px;margin-top:2px}
  .section__list li{position:relative;padding-left:6px}
  .section__list li::before{content:"•";position:absolute;left:0}

  .flyer--en .section--intro{left:28px;top:361px;width:225px}
  .flyer--nl .section--intro{left:28px;top:355px;width:225px}
  .section--paradise{left:281px;top:436px;width:172px}
  .section--passion{left:28px;top:536px;width:245px}

  .contact{position:absolute;left:28px;top:636px;width:421px;border-top:1px solid var(--sky);padding-top:8px;display:flex;justify-content:space-between;font-size:9px;color:var(--navy);letter-spacing:.3px}
  .contact__item{display:flex;align-items:center;gap:7px;white-space:nowrap}
  .contact__item svg{flex:none}
</style>
</head>
<body>

<!-- English side -->
<article class="flyer flyer--en" lang="en">
  <div class="hero">
    <svg viewBox="0 0 480 340" width="480" height="340">
      <defs>
        <linearGradient id="reef-en" x1="0" y1="0" x2="0" y2="1">
          <stop offset="0" stop-color="#4a86cc"/>
          <stop offset="0.45" stop-color="#6a86a8"/>
          <stop offset="0.8" stop-color="#a9a49a"/>
          <stop offset="1" stop-color="#c8c2b6"/>
        </linearGradient>
        <linearGradient id="panel-en" x1="1" y1="0" x2="0" y2="1">
          <stop offset="0" stop-color="#1d8fd8"/>
          <stop offset="0.5" stop-color="#27b2e4"/>
          <stop offset="1" stop-color="#1e7dd0"/>
        </linearGradient>
      </defs>
      <rect role="img" aria-label="Underwater photo of a Bonaire reef with soft corals and a school of fish" x="0" y="0" width="480" height="335" fill="url(#reef-en)"/>
      <path d="M300,0 C340,42 410,80 480,82 L480,0 Z" fill="#2fb8e6"/>
      <path d="M336,0 C375,40 425,72 480,75 L480,0 Z" fill="#fff"/>
      <path d="M480,122 C405,125 375,175 352,225 C330,268 292,290 250,300 L480,300 Z" fill="url(#panel-en)"/>
      <path d="M0,222 C30,262 120,300 250,300 L250,340 L0,340 Z" fill="var(--navy)"/>
      <path d="M0,316 C90,345 200,330 290,300 C370,272 430,275 480,292 L480,340 L0,340 Z" fill="#1e8ed6"/>
      <path d="M0,322 C100,352 210,338 300,306 C375,282 430,284 480,300 L480,340 L0,340 Z" fill="#fff"/>
    </svg>
    <div class="brand"><span class="brand__dot"></span><span class="brand__name">Reef Guild</span></div>
    <h1 class="title"><span class="title__small">THE</span><span class="title__big">CARIBEAN</span></h1>
    <p class="tagline">Easy to come dive with us, just takes half a day</p>
    <p class="callout">Stop by at<br>our Front office<br>and we are happy<br>to answer all your<br>questions or to book your<br>'First Breath Dive'!</p>
    <div class="social" aria-label="Social media"><span class="social__dot"></span><span class="social__dot"></span><span class="social__dot"></span></div>
  </div>

  <div class="photo photo--gear" role="img" aria-label="Photo of scuba gear and tanks resting on a rock by the beach"></div>
  <div class="photo photo--truck" role="img" aria-label="Photo of two divers standing beside a white pick-up truck on a Bonaire shore"></div>
  <div class="photo photo--turtle" role="img" aria-label="Photo of a sea turtle over a coral reef with the Kelp Dive name"></div>

  <section class="section section--intro">
    <h2 class="section__head">First Breath Diving in Bonaire</h2>
    <p class="section__body">Fall in love with diving in our underwater paradise. Under the guidance of a dive instructor you will learn the basic skills for peaceful diving in a fun and easy way.</p>
  </section>

  <section class="section section--paradise">
    <h2 class="section__head">Underwater Paradise</h2>
    <p class="section__body">Bonaire is the place to learn how to scuba dive. After a brief introduction we will directly dive into the sea, where the reef starts in shallow waters. We know the perfect dive sites for beginners. Here, the sea bed slopes gradually down and you'll be amazed by the most beautiful fish and corals.</p>
  </section>

  <section class="section section--passion">
    <h2 class="section__head">Develop a passion for marine life</h2>
    <ul class="section__list">
      <li>Ages 10 and up can sign up for our first breath dive</li>
      <li>You'll dive straight into the water after a brief theoretic introduction</li>
      <li>The First Breath Diving course will take 3-4 hours</li>
      <li>Before participating, you are required to fill out a medical questionnaire</li>
      <li>A group consists of a maximum of 4 people</li>
      <li>Experience the splendor of the ocean without much distraction by other divers</li>
      <li>And enjoy a lot of personal attention given by your instructor</li>
    </ul>
  </section>

  <footer class="contact">
    <span class="contact__item"><svg width="12" height="12" viewBox="0 0 24 24"><path d="M6.6 10.8a15 15 0 0 0 6.6 6.6l2.2-2.2c.3-.3.7-.4 1-.2 1.1.4 2.3.6 3.6.6.6 0 1 .4 1 1V20c0 .6-.4 1-1 1A17 17 0 0 1 3 4c0-.6.4-1 1-1h3.5c.6 0 1 .4 1 1 0 1.3.2 2.5.6 3.6.1.3 0 .7-.2 1z" fill="var(--sky)"/></svg>+0000000 000 000</span>
    <span class="contact__item"><svg width="12" height="12" viewBox="0 0 24 24"><path d="M2 9l10-6 10 6v12H2z" fill="var(--sky)"/><path d="M4 10l8 5 8-5" stroke="#fff" stroke-width="1.6" fill="none"/></svg>company@email.com</span>
    <span class="contact__item"><svg width="13" height="13" viewBox="0 0 24 24" fill="none" stroke="var(--sky)" stroke-width="1.8"><circle cx="12" cy="12" r="10"/><ellipse cx="12" cy="12" rx="4.5" ry="10"/><path d="M2 12h20M4 7h16M4 17h16"/></svg>www.company.com</span>
  </footer>
</article>

<!-- Dutch side -->
<article class="flyer flyer--nl" lang="nl">
  <div class="hero">
    <svg viewBox="0 0 480 340" width="480" height="340">
      <defs>
        <linearGradient id="reef-nl" x1="0" y1="0" x2="0" y2="1">
          <stop offset="0" stop-color="#4a86cc"/>
          <stop offset="0.45" stop-color="#6a86a8"/>
          <stop offset="0.8" stop-color="#a9a49a"/>
          <stop offset="1" stop-color="#c8c2b6"/>
        </linearGradient>
        <linearGradient id="panel-nl" x1="1" y1="0" x2="0" y2="1">
          <stop offset="0" stop-color="#1d8fd8"/>
          <stop offset="0.5" stop-color="#27b2e4"/>
          <stop offset="1" stop-color="#1e7dd0"/>
        </linearGradient>
      </defs>
      <rect role="img" aria-label="Underwater photo of a Bonaire reef with soft corals and a school of fish" x="0" y="0" width="480" height="335" fill="url(#reef-nl)"/>
      <path d="M300,0 C340,42 410,80 480,82 L480,0 Z" fill="#2fb8e6"/>
      <path d="M336,0 C375,40 425,72 480,75 L480,0 Z" fill="#fff"/>
      <path d="M480,122 C405,125 375,175 352,225 C330,268 292,290 250,300 L480,300 Z" fill="url(#panel-nl)"/>
      <path d="M0,222 C30,262 120,300 250,300 L250,340 L0,340 Z" fill="var(--navy)"/>
      <path d="M0,316 C90,345 200,330 290,300 C370,272 430,275 480,292 L480,340 L0,340 Z" fill="#1e8ed6"/>
      <path d="M0,322 C100,352 210,338 300,306 C375,282 430,284 480,300 L480,340 L0,340 Z" fill="#fff"/>
    </svg>
    <div class="brand"><span class="brand__dot"></span><span class="brand__name">Reef Guild</span></div>
    <h1 class="title"><span class="title__small">THE</span><span class="title__big">CARIBEAN</span></h1>
    <p class="tagline">Easy to come dive with us, just takes half a day</p>
    <p class="callout">Kom gerust<br>langs bij onze<br>front-office. Wij zijn<br>graag bereid je vragen<br>te beantwoorden of om<br>de 'First Breath Dive'<br>in te plannen.</p>
    <div class="social" aria-label="Sociale media"><span class="social__dot"></span><span class="social__dot"></span><span class="social__dot"></span></div>
  </div>

  <div class="photo photo--gear" role="img" aria-label="Foto van duikuitrusting op een rots aan het strand"></div>
  <div class="photo photo--truck" role="img" aria-label="Foto van twee duikers naast een witte pick-up op de kust van Bonaire"></div>
  <div class="photo photo--turtle" role="img" aria-label="Foto van een zeeschildpad boven het koraalrif met de naam Kelp Dive"></div>

  <section class="section section--intro">
    <h2 class="section__head">Proefduik op Bonaire</h2>
    <p class="section__body">Word verliefd op het gevoel van duiken in een onderwaterparadijs.<br>Onder begeleiding van een duikinstructeur ontdek je op een makkelijke en leuke manier alle basisvaardigheden voor een heerlijke duik.</p>
  </section>

  <section class="section section--paradise">
    <h2 class="section__head">Onderwaterparadijs</h2>
    <p class="section__body">Bonaire is bij uitstek de plek voor een proefduik. Na een korte introductie stappen we direct de zee in waar het rif al vrij snel begint. Bovendien kennen we de perfecte duikspots voor beginners. Hier loopt de zeebodem in een langzaam tempo naar beneden en word je verrast door de mooiste vissen en koralen.</p>
  </section>

  <section class="section section--passion">
    <h2 class="section__head">Liefde voor het waterleven</h2>
    <ul class="section__list">
      <li>Onze proefduik is voor iedereen vanaf 10 jaar</li>
      <li>Na een korte theoretische introductie geniet je meteen van een duik</li>
      <li>De activiteit duurt 3 tot 4 uur</li>
      <li>Je kunt meedoen wanneer je gezond genoeg bent om jouw duikset te dragen</li>
      <li>Een groep bestaat uit maximaal 4 personen</li>
      <li>Hierdoor ervaar je de pracht van de oceaan zonder afleiding van anderen</li>
      <li>En heeft de duikinstructeur veel tijd voor persoonlijke aandacht</li>
    </ul>
  </section>

  <footer class="contact">
    <span class="contact__item"><svg width="12" height="12" viewBox="0 0 24 24"><path d="M6.6 10.8a15 15 0 0 0 6.6 6.6l2.2-2.2c.3-.3.7-.4 1-.2 1.1.4 2.3.6 3.6.6.6 0 1 .4 1 1V20c0 .6-.4 1-1 1A17 17 0 0 1 3 4c0-.6.4-1 1-1h3.5c.6 0 1 .4 1 1 0 1.3.2 2.5.6 3.6.1.3 0 .7-.2 1z" fill="var(--sky)"/></svg>+0000000 000 000</span>
    <span class="contact__item"><svg width="12" height="12" viewBox="0 0 24 24"><path d="M2 9l10-6 10 6v12H2z" fill="var(--sky)"/><path d="M4 10l8 5 8-5" stroke="#fff" stroke-width="1.6" fill="none"/></svg>company@email.com</span>
    <span class="contact__item"><svg width="13" height="13" viewBox="0 0 24 24" fill="none" stroke="var(--sky)" stroke-width="1.8"><circle cx="12" cy="12" r="10"/><ellipse cx="12" cy="12" rx="4.5" ry="10"/><path d="M2 12h20M4 7h16M4 17h16"/></svg>www.company.com</span>
  </footer>
</article>

</body>
</html>
```